Business Card Design for Cybersecurity Company - Quorvent Systems

We need a business card design for our new cybersecurity company, Quorvent. We’re going for a clean, hi tech look that feels modern, premium, and trustworthy. We want a design that really stands out and makes people say WOW when we hand it over!

Quorvent delivers reliable IT support and managed services for small and mid sized businesses. We help companies stay secure, efficient, and connected through proactive monitoring, cybersecurity services, cloud management, and remote support.

Target Market(s)

Designers should target small and mid sized businesses that need dependable cybersecurity and IT support.

Industry/Entity Type

Cybersecurity, Managed Service Provider, IT services

Contact Information for Business Card

Contact information

Requirements
Must have
• The card should look clean, modern, and tech focused, with the Quorvent logo, clear contact info, and strong readability. It needs to feel premium and professional while still keeping a simple layout that fits a cybersecurity and IT brand.
Nice to have
• Nice to have elements include subtle touches that give the card a modern, tech feel, along with a layout that works well in different background styles.
Should not have
• The card should avoid clutter, loud graphics, or anything that takes attention away from the logo and contact details.

```html
<!DOCTYPE html>
<html lang="en">
<head>
<meta charset="utf-8">
<title>Quorvent Systems – Business Card</title>
<link href="https://fonts.googleapis.com/css2?family=Montserrat:wght@400;500;700;800&display=swap" rel="stylesheet">
<style>
  :root {
    --page: #3a3a3c;
    --card: #1b1b1d;
    --card-edge: #262628;
    --white: #f4f4f6;
    --blue: #3760f6;
    --violet: #7b2ee8;
    --muted: #e6e6ea;
  }
  * { box-sizing: border-box; margin: 0; padding: 0; }
  html, body { width: 1200px; height: 694px; overflow: hidden; }
  body {
    background: var(--page);
    font-family: "Montserrat", Arial, sans-serif;
    position: relative;
  }
  .card {
    position: absolute;
    width: 540px;
    height: 310px;
    background: var(--card);
    border: 1px solid var(--card-edge);
    border-radius: 16px;
    box-shadow: 0 18px 40px rgba(0,0,0,.45);
    overflow: hidden;
  }
  .card--front { left: 50px; top: 60px; }
  .card--back { left: 610px; top: 324px; }

  /* front */
  .front-brand {
    position: absolute; left: 0; right: 0; top: 108px;
    display: flex; align-items: center; justify-content: center; gap: 18px;
  }
  .brand-mark {
    width: 58px; height: 58px; border-radius: 50%;
    background: linear-gradient(135deg, var(--blue), var(--violet));
  }
  .brand-name { color: var(--white); font-weight: 700; line-height: 1; }
  .brand-name__main { display: block; font-size: 46px; letter-spacing: .5px; }
  .brand-name__sub { display: block; font-size: 17px; letter-spacing: 11px; margin-top: 8px; }

  /* back */
  .accent-bar {
    position: absolute; right: 22px; top: 26px; width: 6px; height: 48px;
    background: linear-gradient(180deg, var(--violet), var(--blue));
  }
  .person { position: absolute; right: 40px; top: 28px; text-align: right; }
  .person__name {
    font-size: 24px; font-weight: 800; letter-spacing: .3px;
    background: linear-gradient(90deg, var(--blue), var(--violet));
    -webkit-background-clip: text; background-clip: text; color: transparent;
  }
  .person__title { color: var(--white); font-size: 13px; font-weight: 500; margin-top: 4px; }

  .back-brand { position: absolute; left: 34px; top: 112px; color: var(--blue); font-weight: 700; line-height: 1; }
  .back-brand__main { display: block; font-size: 34px; }
  .back-brand__sub { display: block; font-size: 13px; letter-spacing: 8px; margin-top: 6px; }

  .address { position: absolute; left: 72px; top: 190px; color: var(--muted); font-size: 12.5px; line-height: 1.45; }
  .contacts { position: absolute; left: 72px; top: 228px; list-style: none; color: var(--muted); font-size: 12.5px; }
  .contacts li { display: flex; align-items: center; gap: 7px; height: 18px; }
  .contacts svg { width: 12px; height: 12px; flex: none; }
</style>
</head>
<body>

<section class="card card--front" aria-label="Card front">
  <div class="front-brand">
    <span class="brand-mark" aria-hidden="true"></span>
    <span class="brand-name">
      <span class="brand-name__main">Quorvent</span>
      <span class="brand-name__sub">Systems</span>
    </span>
  </div>
</section>

<section class="card card--back" aria-label="Card back">
  <span class="accent-bar" aria-hidden="true"></span>
  <div class="person">
    <p class="person__name">DANA WHITLOCK</p>
    <p class="person__title">Owner | CEO</p>
  </div>

  <div class="back-brand">
    <span class="back-brand__main">Quorvent</span>
    <span class="back-brand__sub">Systems</span>
  </div>

  <p class="address">PO Box 58210<br>Orlando, FL 32801</p>

  <ul class="contacts">
    <li>
      <svg viewBox="0 0 12 12" aria-hidden="true"><path d="M2 1h2.5l1 2.5-1.5 1a6 6 0 0 0 3.5 3.5l1-1.5 2.5 1V11A9 9 0 0 1 1 2z" fill="var(--violet)"/></svg>
      (855) 430-QVNT
    </li>
    <li>
      <svg viewBox="0 0 12 12" aria-hidden="true"><rect x="3" y="0.8" width="6" height="10.4" rx="1.2" fill="none" stroke="var(--violet)" stroke-width="1.2"/></svg>
      (407) 555-0186
    </li>
    <li>
      <svg viewBox="0 0 12 12" aria-hidden="true"><rect x="0.8" y="2.5" width="10.4" height="7" fill="var(--violet)"/><path d="M0.8 2.5 6 6.5l5.2-4" fill="none" stroke="var(--card)" stroke-width="1"/></svg>
      dana@quorvent.com
    </li>
    <li>
      <svg viewBox="0 0 12 12" aria-hidden="true"><circle cx="6" cy="6" r="5" fill="var(--violet)"/><path d="M1 6h10M6 1c-2 2.5-2 7.5 0 10M6 1c2 2.5 2 7.5 0 10" fill="none" stroke="var(--card)" stroke-width=".8"/></svg>
      quorvent.com
    </li>
  </ul>
</section>

</body>
</html>
```